Corporate-Design für Handwerks- und Dienstleistungsfirma
Erster Vorschlag Logo hat mich nicht mehr losgelassen. Meine Wünsche wurden sehr schnell erfasst und umgesetzt, Top Service Besten Dank!
Zielgruppe
Ich gründe eine Einzelfirma und biete Dienstleistungen im Bereich Handwerk jeglicher Art, mit Schwerpunkt Holz. Zielgruppe Privatpersonen, Verwaltungen etc.
Aufgabenstellung
Den Namen Handwerk und Dienstleistung sollen im Vordergrund stehen, Name, Telefon, E Mail eher Zweitrangig, muss aber bei einem Einzelunternehmen aufgeführt werden.

```html
<!DOCTYPE html>
<html lang="de">
<head>
<meta charset="utf-8">
<title>Fagus Holz und Haus – Visitenkarte</title>
<link rel="stylesheet" href="https://fonts.googleapis.com/css2?family=Montserrat:wght@300;400;600&display=swap">
<style>
  :root {
    --page: #e9e9e9;
    --wood-dark: #2a211b;
    --wood-mid: #4a3a2f;
    --wood-light: #5c4a3d;
    --ink: #f4f1ec;
    --ink-soft: #d9d2c8;
    --mark-faint: #6d5a4b;
  }
  html, body {
    margin: 0;
    width: 1200px;
    height: 898px;
    overflow: hidden;
    background: var(--page);
    font-family: "Montserrat", Arial, sans-serif;
  }
  .sheet {
    width: 1200px;
    height: 898px;
    display: flex;
    flex-direction: column;
    align-items: center;
    justify-content: center;
    gap: 40px;
  }
  .card {
    position: relative;
    width: 660px;
    height: 370px;
    border-radius: 4px;
    overflow: hidden;
    box-shadow: 0 6px 18px rgba(0,0,0,.25);
    color: var(--ink);
  }
  .card__wood {
    position: absolute;
    inset: 0;
    background:
      linear-gradient(95deg, rgba(0,0,0,.25), rgba(255,255,255,.04) 45%, rgba(0,0,0,.3)),
      linear-gradient(180deg, var(--wood-light), var(--wood-mid) 40%, var(--wood-dark));
  }
  .card__content { position: absolute; inset: 0; }

  /* front */
  .brand {
    position: absolute;
    left: 44px;
    top: 58px;
    display: flex;
    align-items: center;
    gap: 14px;
  }
  .brand__square {
    width: 40px;
    height: 40px;
    background: var(--ink);
  }
  .brand__name {
    display: flex;
    flex-direction: column;
    font-weight: 600;
    text-transform: uppercase;
    line-height: 1;
  }
  .brand__line1 { font-size: 26px; letter-spacing: 1px; }
  .brand__line2 { font-size: 15px; letter-spacing: 1.2px; margin-top: 3px; }
  .holder {
    position: absolute;
    left: 190px;
    top: 148px;
    font-weight: 400;
    font-size: 32px;
    letter-spacing: 1.5px;
    text-transform: uppercase;
    white-space: nowrap;
  }
  .holder__first {
    border-bottom: 3px solid var(--ink);
    padding-bottom: 4px;
  }
  .contact {
    position: absolute;
    right: 40px;
    top: 212px;
    text-align: right;
    font-weight: 300;
    font-size: 17px;
    line-height: 1.9;
    color: var(--ink-soft);
    letter-spacing: .5px;
    white-space: nowrap;
  }

  /* back */
  .back-brand {
    display: flex;
    align-items: center;
    justify-content: center;
    gap: 20px;
  }
  .back-brand__square {
    width: 64px;
    height: 64px;
    background: var(--mark-faint);
  }
  .back-brand__name {
    display: flex;
    flex-direction: column;
    font-weight: 600;
    text-transform: uppercase;
    color: var(--mark-faint);
    line-height: 1;
  }
  .back-brand__line1 { font-size: 44px; letter-spacing: 2px; }
  .back-brand__line2 { font-size: 22px; letter-spacing: 2px; margin-top: 4px; }
</style>
</head>
<body>
<main class="sheet">
  <section class="card card--front">
    <div class="card__wood" role="img" aria-label="Dunkle Holzmaserung als Kartenhintergrund"></div>
    <div class="card__content">
      <div class="brand">
        <span class="brand__square"></span>
        <span class="brand__name">
          <span class="brand__line1">Fagus</span>
          <span class="brand__line2">Holz und Haus</span>
        </span>
      </div>
      <div class="holder"><span class="holder__first">Bruno</span> Kell</div>
      <div class="contact">
        <div class="contact__phone">+41 79 000 12 34</div>
        <div class="contact__mail">kellbrunofix@musterwerkstatt.de</div>
      </div>
    </div>
  </section>

  <section class="card card--back">
    <div class="card__wood" role="img" aria-label="Dunkle Holzmaserung als Kartenhintergrund"></div>
    <div class="card__content back-brand">
      <span class="back-brand__square"></span>
      <span class="back-brand__name">
        <span class="back-brand__line1">Fagus</span>
        <span class="back-brand__line2">Holz und Haus</span>
      </span>
    </div>
  </section>
</main>
</body>
</html>
```